RideMatcher.net

We require the look and feel creating for a new website which will allow customers to request & compare airport to resort transport transfers.
The design can be delivered as a one page graphic which our developer will use as a brief when building the website.
Resort destinations would include beach, city & ski.
The above elements should appear in the masthead.
We will also require a logo creating for the site, *perhaps* combing the company name (ridematcher.net) with a car, minibus & aeroplane along with our strapline "Journey on a Budget".
Key phrases which illustrate the type of design we would like are;
Clean, simple, playful, icons (clipart style), professional, bright, big\bold call to action
A few sites we like are;
http://www.pelmotrucks.example/
- especially the clean, playful icons under "Our Services" on the home page
http://www.quotewisp.example/
- but not the background photo!
http://www.lakeshuttlo.example/
a competitor - we feel the homepage is too busy
http://www.artfolkhub.example/
Large icons, clean and clear design.
The site should be 960px wide and centered on the page.
Our developer will use your design to create a flexible bootstrap mobile friendly site using html, css, jquery with a c# mvc mssql backend.
The page should include additional standard\common html elements such as a form, list, div, h1, h2, paragraph etc. This will form the corporate design guidelines for future pages the developer may be asked to create.
Reason: Loving the designs, just need a few more options and streamlining - making this payment guaranteed project because we love the responses so far and looking forward to choosing one of your designs.
Reason: Developer currently away so need to extend until returns to office to decide on a design.
Holiday makers making independent travel arrangements
Building

```html
<!DOCTYPE html>
<html lang="en">
<head>
<meta charset="utf-8">
<title>RideMatcher.net – Journey on a Budget</title>
<link rel="stylesheet" href="https://fonts.googleapis.com/css2?family=Jost:wght@300;400;500;600&family=Open+Sans:wght@400;600;700&display=swap">
<style>
:root{
  --blue:#1e7fc6;
  --blue-dark:#14578f;
  --sky:#2f8fdc;
  --orange:#f2a10f;
  --orange-dark:#d98508;
  --navy:#1a4f8a;
  --text:#444;
  --muted:#666;
  --panel:#f4f4f4;
  --footer:#262626;
}
*{box-sizing:border-box;margin:0;padding:0}
html,body{width:932px;height:1200px;overflow:hidden}
body{position:relative;background:#fff;font-family:"Open Sans",sans-serif;color:var(--text)}
.abs{position:absolute}

/* header */
.site-header{position:absolute;left:0;top:0;width:932px;height:82px;background:linear-gradient(#fff,#f1f1f1);border-bottom:1px solid #ddd}
.brand{left:38px;top:44px;font-family:"Jost",sans-serif;font-weight:500;font-size:23px;color:var(--blue);display:flex;align-items:center;gap:8px}
.brand-dot{width:12px;height:12px;background:var(--orange)}
.strapline{left:278px;top:46px;padding-left:10px;border-left:1px solid #ccc;font-family:"Jost",sans-serif;font-size:18px;color:var(--blue);height:30px;line-height:28px}
.main-nav{right:50px;top:46px;display:flex;align-items:center;font-size:10px;font-weight:700;color:var(--blue-dark)}
.main-nav a{color:inherit;text-decoration:none;padding:0 12px;line-height:24px}
.main-nav .sep{color:var(--blue-dark)}
.main-nav a.active{background:var(--orange);color:#fff;width:56px;text-align:center;padding:0}

/* hero */
.hero{left:0;top:82px;width:932px;height:404px;background:linear-gradient(180deg,#1f5fb3 0%,#2f8fdc 55%,#4aa3e6 80%,#0a0a0a 80.5%,#000 100%)}
.hero-search{right:51px;top:82px;width:238px;height:43px;background:#fff;border-radius:0 0 10px 10px;box-shadow:0 1px 3px rgba(0,0,0,.2)}
.hero-search .field{position:absolute;left:9px;top:8px;width:192px;height:24px;border:2px solid #ccc;border-radius:4px;background:#f3f3f3;font-size:8px;color:#666;text-align:center;line-height:20px}
.hero-search svg{position:absolute;right:10px;top:11px}
.search-area{left:69px;top:214px;width:256px;height:216px;background:rgba(30,80,150,.75)}
.search-area h2{font-family:"Jost",sans-serif;font-weight:300;font-size:22px;color:#fff;text-align:center;padding-top:8px;margin:0 10px;height:40px;border-bottom:1px dashed rgba(255,255,255,.4)}
.pill{position:absolute;left:10px;width:226px;height:27px;border-radius:14px;border:1px solid rgba(255,255,255,.35);background:rgba(15,50,110,.6);font-size:9.5px;font-weight:700;color:#fff;padding-left:15px;line-height:25px}
.pill svg{position:absolute;right:13px;top:5px}
.cta{position:absolute;left:48px;top:170px;width:154px;height:32px;border-radius:6px;background:linear-gradient(#f8b628,#e08908);color:#fff;font-weight:700;font-size:11.5px;text-align:center;line-height:32px;letter-spacing:.3px}
.social{left:899px;top:289px;width:33px;height:173px;background:#fff;padding:9px 4px;display:flex;flex-direction:column;gap:3px}
.social span{width:24px;height:24px;display:block}

/* transfer boxes */
.transfer{top:576px;height:160px;color:#fff}
.transfer.eco{left:48px;width:405px;background:linear-gradient(#37a4ec,#1e7fc6)}
.transfer.private{left:478px;width:403px;background:linear-gradient(#e9ad22,#d57f0a)}
.transfer .pic{position:absolute;top:20px;width:110px;height:90px}
.transfer h1{position:absolute;top:8px;font-family:"Jost",sans-serif;font-weight:400;font-size:23px;letter-spacing:.3px;display:flex;align-items:center;gap:6px}
.tag{font-family:"Open Sans",sans-serif;font-size:10px;font-weight:600;background:rgba(255,255,255,.3);padding:3px 8px;color:#fff}
.tag.dark{background:#e2e2e2;color:#444;font-size:11px}
.transfer p{position:absolute;top:50px;width:243px;font-size:9.5px;line-height:16.5px;text-align:justify}
.transfer .more{position:absolute;left:0;right:0;bottom:0;height:23px;border-top:1px solid rgba(255,255,255,.25);background:rgba(0,0,0,.06);font-size:10.5px;letter-spacing:.4px;line-height:23px}
.swap{left:431px;top:622px;width:76px;height:76px;border-radius:50%;background:#fff}

/* content */
.content{left:0;top:775px;width:932px;height:367px;background:var(--panel)}
.h2{font-family:"Jost",sans-serif;font-size:17px;color:var(--orange);display:flex;align-items:center;gap:6px}
.h2 b{color:var(--blue);font-weight:600}
.rule{height:1px;background:#e0e0e0}
.body-text{font-size:8.5px;line-height:16.4px;text-align:justify;color:var(--text)}
.h3{font-family:"Open Sans",sans-serif;font-weight:600;font-size:12px;color:#333;display:flex;align-items:center;gap:6px}
.bullets{list-style:none;font-size:9.5px;color:var(--text)}
.bullets li{height:22.4px;padding-left:18px;position:relative}
.bullets li::before{content:"";position:absolute;left:4px;top:4px;border-left:4px solid var(--blue);border-top:3px solid transparent;border-bottom:3px solid transparent}
.input{position:absolute;left:638px;width:222px;height:27px;border:1px solid #ccc;border-radius:3px;background:#eee;font-size:8.5px;color:#444;padding:8px 8px}
.submit{left:639px;top:1069px;width:82px;height:22px;border-radius:3px;background:linear-gradient(#f8c040,#e39b10);border:1px solid #c8870c;font-size:10px;font-weight:700;color:#333;text-align:center;line-height:20px}

/* footer */
.site-footer{left:0;top:1142px;width:932px;height:58px;background:linear-gradient(#3a3a3a,#1e1e1e);color:#fff;text-align:center}
.site-footer nav{padding-top:20px;font-size:10px;font-weight:700;display:flex;justify-content:center;gap:15px}
.site-footer small{display:block;font-size:8.5px;margin-top:7px;color:#eee}
</style>
</head>
<body>

<header class="site-header">
  <div class="abs brand"><span class="brand-dot"></span>RideMatcher.net</div>
  <div class="abs strapline">Journey on a Budget</div>
  <nav class="abs main-nav">
    <a class="active" href="#">Agents</a><span class="sep">|</span>
    <a href="#">My Booking</a><span class="sep">|</span>
    <a href="#">Destinations</a><span class="sep">|</span>
    <a href="#" style="padding-right:0">Travel offers</a>
  </nav>
</header>

<section class="abs hero" role="img" aria-label="Night sky over a city skyline with an aeroplane in flight and a yellow taxi facing forward"></section>

<div class="abs hero-search">
  <div class="field">----Search your keyword------</div>
  <svg width="18" height="18" viewBox="0 0 18 18"><circle cx="7" cy="7" r="5" fill="#5aaef0" stroke="#1e6fb8" stroke-width="2"/><line x1="11" y1="11" x2="16" y2="16" stroke="#1e6fb8" stroke-width="3" stroke-linecap="round"/></svg>
</div>

<form class="abs search-area">
  <h2>Search Area</h2>
  <div class="pill" style="top:53px">Pick up from</div>
  <div class="pill" style="top:90px">Place to</div>
  <div class="pill" style="top:128px">By Date
    <svg width="16" height="16" viewBox="0 0 16 16"><rect x="1" y="2" width="14" height="13" rx="2" fill="#fff"/><rect x="1" y="2" width="14" height="4" rx="1" fill="#f08a1a"/><circle cx="8" cy="10.5" r="2.5" fill="#f08a1a"/></svg>
  </div>
  <div class="cta">DELIVERIES FROM £19</div>
</form>

<aside class="abs social" aria-label="Social links">
  <span style="background:#3b5998"></span>
  <span style="background:#e8612c"></span>
  <span style="background:#333"></span>
  <span style="background:#2aa9e0"></span>
  <span style="background:#c4302b"></span>
  <span style="background:#2b9fe0"></span>
</aside>

<article class="abs transfer eco">
  <div class="pic" style="left:0" role="img" aria-label="White minibus"><div style="width:100%;height:100%;background:linear-gradient(#f4f6f8,#b9c2cb);border-radius:12px 30px 6px 6px"></div></div>
  <h1 style="left:128px">Eco TRANSFER <svg width="30" height="8"><line x1="0" y1="4" x2="24" y2="4" stroke="#fff"/><path d="M22 0l7 4-7 4z" fill="#fff"/></svg><span class="tag">{h1}</span></h1>
  <p style="left:128px">Lorem ipsum dolor sit amet, consectetur adipiscing elit. Nunc magna felis, hendrerit non erat sed, dictum viverra enim. Vivamus accumsan pretium nulla, nec faucibus risus lacinia vel. Integer ut mi eu metus venenatis porttitor ac ac enim...</p>
  <div class="more" style="padding-left:128px">Click on the box to expand details <svg width="13" height="13" style="vertical-align:-2px"><circle cx="6.5" cy="6.5" r="6" fill="#fff"/><path d="M5 3.5l3.5 3-3.5 3z" fill="#555"/></svg></div>
</article>

<article class="abs transfer private">
  <h1 style="left:40px">Private TRANSFER <svg width="30" height="8"><line x1="0" y1="4" x2="24" y2="4" stroke="#fff"/><path d="M22 0l7 4-7 4z" fill="#fff"/></svg><span class="tag">{h1}</span></h1>
  <p style="left:40px">Lorem ipsum dolor sit amet, consectetur adipiscing elit. Nunc magna felis, hendrerit non erat sed, dictum viverra enim. Vivamus accumsan pretium nulla, nec faucibus risus lacinia vel. Integer ut mi eu metus venenatis porttitor ac ac enim...</p>
  <div class="pic" style="right:0" role="img" aria-label="Yellow taxi cab"><div style="width:100%;height:100%;background:linear-gradient(#ffe040,#e8b800);border-radius:30px 14px 10px 10px"></div></div>
  <div class="more" style="padding-left:101px">Click on the box to expand details <svg width="13" height="13" style="vertical-align:-2px"><circle cx="6.5" cy="6.5" r="6" fill="#fff"/><path d="M5 3.5l3.5 3-3.5 3z" fill="#555"/></svg></div>
</article>

<div class="abs swap">
  <svg width="76" height="76" viewBox="0 0 76 76"><path d="M20 32h28v-7l12 10-12 10v-7H20z" fill="#1e7fc6"/><path d="M56 44H28v-7L16 47l12 10v-7h28z" fill="#e39510"/></svg>
</div>

<section class="abs content"></section>

<div class="abs h2" style="left:44px;top:790px">Overview About <b>RIDEMATCHER</b>
  <svg width="30" height="8"><line x1="0" y1="4" x2="24" y2="4" stroke="#555"/><path d="M22 0l7 4-7 4z" fill="#555"/></svg><span class="tag dark">{h2}</span></div>
<div class="abs rule" style="left:44px;top:820px;width:560px"></div>
<p class="abs body-text" style="left:44px;top:832px;width:374px">Nulla lobortis ligula faucibus orci pharetra, a adipiscing nunc posuere. Fusce eu malesuada ligula. Etiam eu tortor eros. Nam sollicitudin nec massa vel malesuada. Praesent nisl massa, suscipit viverra sapien id, cursus pretium nisl. Nullam sit amet mi mi. Etiam feugiat feugiat suscipit. In nec tempor mauris, nec venenatis urna. Vestibulum neque quam, luctus in nibh vel, porta suscipit justo. Vestibulum dapibus nisl id feugiat iaculis.<br>Mauris varius lectus vitae tortor dapibus aliquet. Quisque ut bibendum sapien. Nunc placerat turpis sed libero convallis mattis. Aenean at posuere enim. Morbi a tristique nunc...</p>
<div class="abs" style="left:431px;top:833px;width:177px;height:108px;background:#fff;border:1px solid #e6e6e6;padding:8px" role="img" aria-label="White minibus side view"><div style="width:100%;height:100%;background:linear-gradient(#fafafa,#c9cfd5);border-radius:14px 40px 8px 8px"></div></div>

<div class="abs h3" style="left:44px;top:977px">Unordered List Style
  <svg width="30" height="8"><line x1="0" y1="4" x2="24" y2="4" stroke="#555"/><path d="M22 0l7 4-7 4z" fill="#555"/></svg><span class="tag dark">{h3}</span></div>
<ul class="abs bullets" style="left:45px;top:1004px">
  <li>Proin pharetra tellus ac odio posuere fermentum</li>
  <li>Fusce eu malesuada ligula</li>
  <li>Donec vehicula consectetur condimentum</li>
  <li>Praesent nisl massa, suscipit viverra sapien id</li>
  <li>Vestibulum venenatis, diam id adipiscing vulputate</li>
</ul>

<div class="abs" style="left:619px;top:862px;width:1px;height:280px;background:#ddd"></div>

<div class="abs h2" style="left:641px;top:790px">Quick <b>ENQUIRY</b>
  <svg width="30" height="8"><line x1="0" y1="4" x2="24" y2="4" stroke="#555"/><path d="M22 0l7 4-7 4z" fill="#555"/></svg><span class="tag dark">{h2}</span></div>
<div class="abs rule" style="left:638px;top:820px;width:240px"></div>
<p class="abs body-text" style="left:638px;top:831px;width:240px;text-align:left">Nam sollicitudin nec massa vel malesuada. Praesent nisl massa, suscipit viverra sapien id, cursus pretium nisl.</p>
<div class="input" style="top:878px">Your Name</div>
<div class="input" style="top:916px">Your Email</div>
<div class="input" style="top:954px">Select Location
  <svg width="8" height="6" style="position:absolute;right:10px;top:11px"><path d="M1 1l3 3 3-3" stroke="#333" stroke-width="1.5" fill="none"/></svg></div>
<div class="input" style="top:992px;height:64px">Your Message</div>
<div class="abs submit">Submit Now</div>

<footer class="abs site-footer">
  <nav><span>Home</span><span>About Us</span><span>Careers</span><span>Contact</span><span>Locations</span><span>Services</span><span>Technology</span></nav>
  <small>Copyright © 2013 ridematcher.net. All Rights Reserved.</small>
</footer>

</body>
</html>
```